Thoroughbred Racing Partnership needs web design

Crest of Fortune Partners is a management group who buys horses and races them on both the West and East coasts. The premise of the business is for an investment as little as $500, anyone can be a partner and own a percentage of a horse(s). This is a low cost way of getting involved in the exciting sport of Thoroughbred Racing, without shouldering the heavy financial responsibility. Our target market is mostly males 40+ but we want to include all target markets. We are looking for something very clean and professional, we want to give an image of success. Nothing overly "artsy." I have included the logo in which you can incorporate in the site. Also, the logo colors will be the colors of our "silks." The silks are what the jockey wears and will be an important marketing tool for COF. We would like a very prominent picture of a racehorse somewhere on the homepage, we want to make it clear that is a website for Horseracing partnerships.

On the top of the site, it should say "Crest of Fortune" (on the top)
and below that "Thoroughbred Racing Partnerships." (below that)

The main sections, which should be across the top are:

Home
About Us
Ownership
Stable Roster
News
Contact us

Some of these will have drop down menus.

An example of a competitor website that we like is: www.harlowfieldeq.example
An example of a competitor website that we don't like is: www.gallopvane.example
Updates

Project Deadline Extended
Reason: We have a Board of Directors meeting on the 22nd and we will be making a decision on that day. I'm giving an extension so that all designers are able to submit their designs by the 22nd. Thank you!

Target Market(s)

40+ males

Industry/Entity Type

Business

Requirements
Must have
• our logo must be on the site. We would like at least one bold image of a thoroughbred horse in action. The picture is going to tell the story so it needs to be very eye-catching.

Our slogan should also be included on the website, "Experience the thrill of owning a Racehorse."
Should not have
• cartoons, artsy pictures, pictures of Steeplechase horses or "jumpers." This partnership is for racehorses only, there is not jumping involved with the horses.

```html
<!DOCTYPE html>
<html lang="en">
<head>
<meta charset="utf-8">
<title>Crest of Fortune Partners</title>
<link rel="stylesheet" href="https://fonts.googleapis.com/css2?family=Montserrat:wght@600;700&family=Arimo:wght@400&display=swap">
<style>
  :root {
    --brand-red: #a6242f;
    --nav-bg: #f4f4f4;
    --ink: #1d1d1d;
    --muted: #8f8f8f;
    --footer-bg: #e4e4e4;
    --white: #ffffff;
    --sky: #6fb0dc;
    --icon-grey: #d6d6d6;
  }
  * { box-sizing: border-box; margin: 0; padding: 0; }
  html, body { width: 1200px; height: 813px; overflow: hidden; background: var(--white); }
  body { position: relative; font-family: "Arimo", Arial, sans-serif; color: var(--ink); }

  .top-band { position: absolute; left: 0; top: 0; width: 1200px; height: 62px; background: var(--brand-red); }
  .nav-bar { position: absolute; left: 0; top: 62px; width: 1200px; height: 40px;
    background: linear-gradient(#ffffff, var(--nav-bg)); box-shadow: 0 2px 4px rgba(0,0,0,.18); z-index: 2; }
  .logo-tab { position: absolute; left: 0; top: 0; width: 1200px; height: 120px; z-index: 3; pointer-events: none; }
  .logo-name { position: absolute; left: 205px; top: 30px; width: 230px; z-index: 4; display: flex; align-items: center; gap: 8px;
    font-family: "Montserrat", sans-serif; font-weight: 700; font-size: 26px; color: var(--brand-red); }
  .logo-name .dot { width: 14px; height: 14px; border-radius: 50%; background: var(--brand-red); flex: none; }

  .site-title { position: absolute; right: 353px; top: 15px; text-align: right; color: var(--white); font-family: "Montserrat", sans-serif; }
  .site-title h1 { font-size: 21px; font-weight: 600; line-height: 24px; letter-spacing: -.2px; }
  .site-title p { font-size: 9.5px; font-weight: 600; line-height: 11px; }
  .title-divider { position: absolute; left: 870px; top: 4px; width: 1px; height: 50px; background: rgba(255,255,255,.35); }
  .social { position: absolute; left: 894px; top: 17px; display: flex; gap: 4px; }
  .social span { width: 27px; height: 27px; border-radius: 50%; background: radial-gradient(circle at 40% 35%, #e6e6e6, var(--icon-grey) 70%, #c4c4c4);
    display: flex; align-items: center; justify-content: center; }

  .main-nav { position: absolute; top: 62px; left: 0; width: 1200px; height: 40px; z-index: 4; font-family: "Montserrat", sans-serif; font-weight: 700; font-size: 11px; color: var(--ink); }
  .main-nav a { position: absolute; top: 17px; color: inherit; text-decoration: none; transform: translateX(-50%); white-space: nowrap; }
  .nav-marker { position: absolute; left: 488px; top: 62px; width: 0; height: 0; border-left: 5px solid transparent; border-right: 5px solid transparent; border-top: 5px solid var(--brand-red); z-index: 5; transform: translateX(-50%); }

  .hero { position: absolute; left: 0; top: 102px; width: 1200px; height: 338px;
    background:
      radial-gradient(ellipse 190px 120px at 420px 200px, rgba(60,30,18,.75), rgba(60,30,18,0) 100%),
      radial-gradient(ellipse 170px 110px at 270px 240px, rgba(45,22,14,.8), rgba(45,22,14,0) 100%),
      radial-gradient(ellipse 120px 80px at 580px 170px, rgba(150,80,40,.6), rgba(150,80,40,0) 100%),
      radial-gradient(ellipse 110px 70px at 110px 180px, rgba(110,55,30,.45), rgba(110,55,30,0) 100%),
      linear-gradient(90deg, rgba(0,0,0,0) 0%, rgba(0,0,0,0) 52%, rgba(111,176,220,.85) 68%, rgba(111,176,220,1) 80%, #a6d2ec 100%),
      linear-gradient(180deg, #5f7f8e 0%, #4d6b5c 7%, #1d2a2f 14%, #1a2328 36%, #8f9c98 42%, #6f8a5c 50%, #8b7864 62%, #9a8470 100%);
  }
  .hero-slogan { position: absolute; left: 738px; top: 174px; width: 300px; font-family: "Montserrat", sans-serif; font-weight: 700; font-size: 34px; line-height: 34px; color: var(--white); text-shadow: 0 2px 3px rgba(0,0,0,.25); letter-spacing: -.3px; }
  .hero-button { position: absolute; left: 735px; top: 297px; width: 279px; height: 61px; border-radius: 6px;
    background: linear-gradient(#5a5a5a, #111111); color: var(--white); display: flex; align-items: center; padding-left: 22px; gap: 14px;
    font-family: "Montserrat", sans-serif; font-weight: 700; font-size: 16px; text-decoration: none; box-shadow: 0 2px 4px rgba(0,0,0,.3); }

  .feature-card { position: absolute; left: 727px; top: 403px; width: 314px; height: 214px; background: var(--white); border-radius: 5px; box-shadow: 0 6px 16px rgba(0,0,0,.18); }
  .feature-photo { position: absolute; left: 9px; top: 8px; width: 298px; height: 197px;
    background:
      radial-gradient(ellipse 70px 60px at 90px 80px, rgba(70,35,20,.7), rgba(70,35,20,0)),
      radial-gradient(ellipse 70px 60px at 180px 70px, rgba(110,60,30,.7), rgba(110,60,30,0)),
      linear-gradient(180deg, #6d5a4a 0%, #7b5b3f 45%, #5f8a3c 78%, #4e7a2f 100%); }

  .welcome { position: absolute; left: 196px; top: 482px; width: 500px; }
  .welcome h2 { font-family: "Montserrat", sans-serif; font-weight: 700; font-size: 21px; color: var(--brand-red); line-height: 28px; letter-spacing: -.2px; }
  .welcome p { margin-top: 7px; font-size: 10.2px; line-height: 18px; color: #2a2a2a; }
  .read-more { position: absolute; left: 593px; top: 578px; font-family: "Montserrat", sans-serif; font-weight: 700; font-size: 13px; color: var(--brand-red); text-decoration: underline; }

  .site-footer { position: absolute; left: 0; top: 660px; width: 1200px; height: 153px; background: var(--footer-bg); }
  .sitemap h3, .footer-contact h3 { font-family: "Montserrat", sans-serif; font-weight: 600; font-size: 17px; color: var(--muted); }
  .sitemap { position: absolute; left: 198px; top: 53px; }
  .sitemap ul { list-style: none; display: grid; grid-template-columns: 90px 89px 90px; row-gap: 5px; margin-top: 8px; font-size: 10.5px; line-height: 13px; }
  .footer-contact { position: absolute; right: 391px; top: 54px; text-align: right; }
  .footer-contact p { margin-top: 8px; font-size: 10.5px; line-height: 17px; }
  .footer-brand { position: absolute; left: 845px; top: 712px; display: flex; align-items: center; gap: 8px; font-family: "Montserrat", sans-serif; font-weight: 700; font-size: 24px; color: #9c9c9c; }
  .footer-brand .dot { width: 14px; height: 14px; border-radius: 50%; background: #9c9c9c; }
</style>
</head>
<body>
  <header>
    <div class="top-band"></div>
    <div class="nav-bar"></div>
    <svg class="logo-tab" viewBox="0 0 1200 120" aria-hidden="true">
      <path d="M95 0 C140 0 150 35 172 58 C190 100 210 114 250 114 L385 114 C425 114 440 98 458 62 C476 20 490 0 520 0 Z" fill="#ffffff"/>
    </svg>
    <div class="logo-name"><span class="dot"></span>COF Partners</div>
    <div class="site-title">
      <h1>Crest of Fortune</h1>
      <p>Thoroughbred Racing Partnerships.</p>
    </div>
    <div class="title-divider"></div>
    <div class="social" aria-label="Social links">
      <span aria-label="Social profile"></span>
      <span aria-label="Social profile"></span>
      <span aria-label="Email"><svg width="15" height="11" viewBox="0 0 15 11"><rect x="0.75" y="0.75" width="13.5" height="9.5" fill="none" stroke="#ffffff" stroke-width="1.5"/><path d="M1 1 L7.5 6 L14 1" fill="none" stroke="#ffffff" stroke-width="1.5"/></svg></span>
      <span aria-label="News feed"></span>
    </div>
    <nav class="main-nav">
      <a href="#" style="left:483px">HOME</a>
      <a href="#" style="left:572px">ABOUT US</a>
      <a href="#" style="left:671px">OWNERSHIP</a>
      <a href="#" style="left:778px">STABLE ROSTER</a>
      <a href="#" style="left:887px">NEWS</a>
      <a href="#" style="left:980px">CONTACT US</a>
    </nav>
    <div class="nav-marker"></div>
  </header>

  <section class="hero" role="img" aria-label="Thoroughbred racehorses with jockeys in red and white silks galloping on a dirt track in front of a tote board, fading into blue sky"></section>
  <p class="hero-slogan">Experience the thrill of owning a Racehorse.</p>
  <a class="hero-button" href="#">Learn About Partnerships
    <svg width="14" height="20" viewBox="0 0 14 20"><path d="M3 2 L11 10 L3 18" fill="none" stroke="#ffffff" stroke-width="3.5" stroke-linecap="round" stroke-linejoin="round"/></svg>
  </a>

  <div class="feature-card">
    <div class="feature-photo" role="img" aria-label="Racehorses and jockeys running close together on a turf course"></div>
  </div>

  <section class="welcome">
    <h2>Welcome to Crest of Fortune Partners</h2>
    <p>Lorem ipsum dolor sit amet, consectetur adipiscing elit. Donec eleifend diam id vulputate dictum. Morbi sagittis dui sit amet ultricies pharetra. Vestibulum sagittis turpis a fermentum interdum. Mauris sapien arcu, sollicitudin at diam eget, posuere lobortis turpis. Morbi nisi odio, congue eu leo a, sollicitudin congue leo.</p>
  </section>
  <a class="read-more" href="#">READ MORE</a>

  <footer class="site-footer">
    <div class="sitemap">
      <h3>Sitemap</h3>
      <ul>
        <li>Home</li><li>Stable Roster</li><li>Ownership</li>
        <li>About Us</li><li>News</li><li>Contact us</li>
      </ul>
    </div>
    <div class="footer-contact">
      <h3>COF Partners</h3>
      <p>Lorem ipsum Street it amet, consectetur adipiscing elit. Donec<br>P: 1800 - 5550 0142, E: email@cofpartners.example</p>
    </div>
  </footer>
  <div class="footer-brand"><span class="dot"></span>COF Partners</div>
</body>
</html>
```